Boutique Financial Services/Advisor Business Needs Web Design

Looking for an informational and functional web design for my Financial Services/Financial Advisement business. It should have functionality for Company name, address, phone #, "About Us", Who we are, Our Mission, Services we offer, Biographies/Photos of/about "The Team", and possibly a link to "Contact Us". Would like to see something new & exciting blended with a traditional/professional look that will appeal to those approaching retirement, as well as those younger clients that are beginning to think about planning for the future. I already have a web domain through HostMeadow, but would like this to be the design we use for that domain.
Financial Services/Financial Advisor
Coded - Design and coding required
1 page

```html
<!DOCTYPE html>
<html lang="en">
<head>
<meta charset="utf-8">
<title>Summitline Wealth Management</title>
<link rel="stylesheet" href="https://fonts.googleapis.com/css2?family=Cormorant+Garamond:wght@500;600&family=Jost:wght@400;500;600&display=swap">
<style>
:root{
  --blue:#0b4aa2;
  --blue-bright:#1457b8;
  --navy:#0c2850;
  --navy-2:#143a70;
  --pale:#c8d8ee;
  --ink:#1d1d1d;
  --body:#3a3a3a;
  --white:#fff;
  --label:#1a4e9c;
}
*{box-sizing:border-box;margin:0;padding:0}
html,body{width:1200px;height:4373px;overflow:hidden}
body{position:relative;font-family:'Jost',sans-serif;color:var(--body);background:var(--white)}
.abs{position:absolute}
section,header,footer,.topbar{position:absolute;left:0;width:1200px;overflow:hidden}
.label{font-family:'Jost',sans-serif;font-weight:500;font-size:14px;letter-spacing:.6px;color:var(--label)}
.h2{font-family:'Cormorant Garamond',serif;font-weight:500;font-size:38px;color:var(--ink);line-height:1.1}
.para{font-size:11.5px;line-height:19px;color:var(--body)}
.btn{display:flex;align-items:center;justify-content:center;font-size:11px;font-weight:500;letter-spacing:.5px;border:1.5px solid var(--blue);color:var(--blue);background:transparent}
.photo{background:linear-gradient(135deg,#7b8896,#c4ccd4)}

.topbar{top:0;height:24px;background:var(--blue);color:#fff;font-size:8px}
.topbar .msg{left:100px;top:7px}
.topbar .msg u{margin-left:3px}
.topbar .soc{top:5px;width:13px;height:13px;border:1px solid #fff;border-radius:50%}

header{top:24px;height:95px;background:#fff}
.nav{top:40px;font-size:12px;letter-spacing:.3px;color:var(--ink);white-space:nowrap}
.nav.active{color:var(--blue)}
.brand{left:490px;top:44px;width:220px;text-align:center;font-family:'Cormorant Garamond',serif;font-weight:600;color:var(--navy);font-size:14px;line-height:15px;white-space:nowrap}
.brand-mark{left:590px;top:14px;width:20px;height:20px;border-radius:50%;background:var(--navy)}

.hero{top:119px;height:562px}
.hero .shade{left:0;top:0;width:700px;height:562px;background:linear-gradient(90deg,rgba(10,25,45,.8),rgba(10,25,45,0))}
.hero .kicker{left:100px;top:156px;font-size:14px;letter-spacing:.8px;color:#8fb4e6}
.hero h1{left:100px;top:186px;font-family:'Cormorant Garamond',serif;font-weight:500;font-size:45px;line-height:52px;color:#fff;white-space:nowrap}
.hero p{left:100px;top:296px;width:400px;font-size:11.5px;line-height:19px;color:#e8edf3}
.hero .btn{left:100px;top:381px;width:124px;height:32px;border-color:#fff;color:#fff}

.about{top:681px;height:653px}
.about .frame{left:100px;top:67px;width:414px;height:457px;background:var(--blue)}
.about .img{left:131px;top:96px;width:500px;height:487px}
.about .label{left:662px;top:132px}
.about .h2{left:662px;top:168px}
.about .p1{left:662px;top:233px;width:440px}
.about .p2{left:662px;top:318px;width:440px}
.about .btn{left:662px;top:491px;width:126px;height:33px}

.services{top:1334px;height:571px;background:linear-gradient(180deg,var(--navy-2),var(--navy))}
.services .label{left:100px;top:54px;color:#fff}
.services .h2{left:100px;top:88px;color:#fff}
.services .intro{left:575px;top:66px;width:525px;font-size:11.5px;line-height:21px;color:#dbe4f2}
.svc-img{top:183px;width:319px;height:187px}
.svc-card{top:332px;width:250px;height:111px;background:#fff}
.svc-card svg{position:absolute;left:20px;top:12px}
.svc-card .t{position:absolute;left:20px;top:50px;font-size:17px;font-weight:500;color:var(--ink)}
.svc-card .r{position:absolute;left:20px;top:82px;font-size:10px;font-weight:600;color:var(--blue);text-decoration:underline}
.arrow{width:22px;height:22px}
.services .btn{left:538px;top:475px;width:124px;height:32px;border-color:#fff;color:#fff}
.dot{top:551px;width:9px;height:9px;border-radius:50%;background:#5d6f8c}

.mission{top:1905px;height:568px}
.mission .label{left:100px;top:73px}
.mission .h2{left:100px;top:100px;font-size:40px;line-height:45px;width:560px}
.mission .p1{left:100px;top:260px;width:430px}
.mission .p2{left:100px;top:346px;width:430px}
.mission .btn{left:100px;top:428px;width:124px;height:32px}

.benefits{top:2473px;height:412px;background:linear-gradient(180deg,var(--navy-2),#1d4478)}
.benefits .label{left:0;width:1200px;text-align:center;top:66px;color:#fff}
.benefits .h2{left:0;width:1200px;text-align:center;top:94px;color:#fff}
.ben{top:156px;width:238px;height:186px;background:#fff;text-align:center}
.ben .ic{position:absolute;left:87px;top:15px;width:64px;height:64px;border-radius:50%;background:var(--blue-bright);display:flex;align-items:center;justify-content:center}
.ben .t{position:absolute;left:0;right:0;top:92px;font-size:17px;font-weight:500;color:var(--ink)}
.ben .d{position:absolute;left:20px;right:20px;top:124px;font-size:10.5px;line-height:18px;color:var(--body)}

.team{top:2885px;height:582px}
.team .label{left:0;width:1200px;text-align:center;top:70px}
.team .h2{left:0;width:1200px;text-align:center;top:100px}
.member{top:175px;width:236px;height:276px}
.member .ph{position:absolute;left:0;top:0;width:236px;height:234px}
.member .bar{position:absolute;left:0;top:234px;width:236px;height:42px;background:var(--blue);color:#fff;display:flex;align-items:center;justify-content:center;font-size:13px;white-space:nowrap}
.member .bar small{font-size:10.5px;color:#cfdcf0;margin-left:6px}
.member .s{position:absolute;left:204px;width:20px;height:20px;border-radius:50%;border:1.5px solid var(--blue);background:#fff}
.team .join{left:0;width:1200px;top:498px;text-align:center;font-size:13px;color:var(--ink)}
.team .join span{color:var(--blue)}

.contact{top:3467px;height:594px;background:linear-gradient(180deg,var(--navy-2),var(--navy))}
.contact .frame{left:100px;top:71px;width:389px;height:459px;background:var(--blue)}
.contact .img{left:137px;top:97px;width:420px;height:395px}
.contact .label{left:601px;top:118px;color:#fff}
.contact .h2{left:601px;top:152px;color:#fff}
.field{height:34px;background:#fff;font-size:9.5px;color:#888;padding:11px 14px}
.contact .submit{left:601px;top:453px;width:112px;height:27px;background:var(--blue-bright);color:#fff;font-size:10px;font-weight:500;display:flex;align-items:center;justify-content:center}

footer{top:4061px;height:312px;background:#fff}
.fbrand{left:90px;top:100px;width:225px;text-align:center;font-family:'Cormorant Garamond',serif;font-weight:600;font-size:18px;line-height:20px;color:var(--navy);white-space:nowrap}
.fbrand-mark{left:183px;top:54px;width:38px;height:38px;border-radius:50%;background:var(--navy)}
.fsoc{top:196px;width:20px;height:20px;border-radius:50%;border:1.5px solid var(--blue)}
.fh{top:56px;font-size:14px;font-weight:500;color:var(--ink)}
.flink{left:392px;font-size:10px;color:var(--ink)}
.finfo{left:597px;display:flex;align-items:flex-start;gap:10px;font-size:10px;line-height:17px;color:var(--ink)}
.finfo .ci{flex:none;width:22px;height:22px;border-radius:50%;background:var(--blue-bright);display:flex;align-items:center;justify-content:center}
.fin{left:872px;top:88px;width:228px;height:36px;border:1px solid #aaa;font-size:9.5px;padding:12px 14px;color:#444}
.fsub{left:872px;top:139px;width:228px;height:30px;background:var(--blue-bright);color:#fff;font-size:10px;font-weight:500;display:flex;align-items:center;justify-content:center}
.fline{left:100px;top:258px;width:1000px;height:1px;background:#bbb}
.copy{left:0;width:1200px;top:276px;text-align:center;font-size:11px;color:var(--ink)}
</style>
</head>
<body>

<div class="topbar">
  <div class="abs msg">Need Free Consultation? <u>Book Schedule Now</u></div>
  <div class="abs soc" style="left:1022px"></div>
  <div class="abs soc" style="left:1040px"></div>
  <div class="abs soc" style="left:1058px"></div>
  <div class="abs soc" style="left:1086px"></div>
</div>

<header>
  <div class="abs nav active" style="left:100px">HOME</div>
  <div class="abs nav" style="left:180px">WHO WE ARE</div>
  <div class="abs nav" style="left:304px">OUR EXPERTISE &amp; SERVICES</div>
  <div class="abs brand-mark"></div>
  <div class="abs brand">SUMMITLINE WEALTH<br>MANAGEMENT</div>
  <div class="abs nav" style="left:737px">OUR TEAM</div>
  <div class="abs nav" style="left:835px">SUCCESS STORIES &amp; NEWS</div>
  <div class="abs nav" style="left:1028px">CONTACT US</div>
</header>

<section class="hero">
  <div class="abs" role="img" aria-label="Photo of a financial advisor with a tablet meeting two smiling clients" style="left:0;top:0;width:1200px;height:562px;background:linear-gradient(90deg,#26323d,#5a6069 55%,#8a8580)"></div>
  <div class="abs shade"></div>
  <svg class="abs" style="left:0;top:0" width="1200" height="562" viewBox="0 0 1200 562" aria-hidden="true">
    <polygon points="960,250 1200,0 1200,562 880,562" fill="#1b57b3" opacity=".55"/>
    <polygon points="0,330 0,562 190,562" fill="#1b57b3" opacity=".35"/>
  </svg>
  <div class="abs kicker">Welcome To Summitline Wealth Management</div>
  <h1 class="abs">Secure Your Financial<br>Future With Confidence.</h1>
  <p class="abs">Expert financial guidance tailored to your goals, whether you're planning for tomorrow or securing your legacy. Personalized strategies for every stage of life—designed to grow with you.</p>
  <div class="abs btn">GET IN TOUCH</div>
</section>

<section class="about">
  <div class="abs frame"></div>
  <div class="abs img photo" role="img" aria-label="Photo of an advisor presenting market charts to colleagues in a meeting room"></div>
  <svg class="abs" style="left:1011px;top:495px" width="189" height="158" aria-hidden="true"><polygon points="105,0 189,158 0,158" fill="var(--pale)"/></svg>
  <div class="abs label">About Summitline Wealth Management</div>
  <div class="abs h2">Who We Are</div>
  <p class="abs para p1">At Summitline Wealth Management, we believe financial success is about more than numbers—it's about creating peace of mind. With &nbsp;years of experience], we are dedicated to guiding clients through every stage of their financial journey, from planning to legacy-building.</p>
  <p class="abs para p2">Lorem Ipsum is simply dummy text of the printing and typesetting industry. Lorem Ipsum has been the industry's standard dummy text ever since the 1500s, when an unknown printer took a galley of type and scrambled it to make a type specimen book. It has survived not only five centuries, but also the leap into electronic typesetting, remaining essentially unchanged. It was popularised in the 1960s with the release of Typeline sheets containing Lorem Ipsum passages, and more recently with desktop publishing software like Layoutworks Pro including versions of Lorem Ipsum.</p>
  <div class="abs btn">LEARN MORE</div>
</section>

<section class="services">
  <div class="abs label">Our Services</div>
  <div class="abs h2">What We Do</div>
  <p class="abs intro">Delivering deep insight game work changing ideas made easy the team work it demonstrates both internally being employees, over 3595 detailers and engineers. Lorem Ipsum Lorem Ipsum is simply dummy text of the printing and typesetting industry.</p>

  <div class="abs svc-img photo" role="img" aria-label="Photo of a retirement plan note with calculator and charts" style="left:100px;background:linear-gradient(135deg,#d9dde3,#8d97a6)"></div>
  <div class="abs svc-img photo" role="img" aria-label="Photo of advisors reviewing a financial dashboard on a laptop" style="left:439px;background:linear-gradient(135deg,#5d6d82,#a7b2c0)"></div>
  <div class="abs svc-img photo" role="img" aria-label="Photo of an advisor meeting a couple in their living room" style="left:778px;background:linear-gradient(135deg,#c9b89a,#8a8f7c)"></div>

  <div class="abs svc-card" style="left:134px">
    <svg width="34" height="32" viewBox="0 0 34 32" fill="none" stroke="var(--blue)" stroke-width="1.8"><rect x="3" y="12" width="18" height="16" rx="2"/><circle cx="12" cy="20" r="4"/><path d="M22 10l6-6M24 4h4v4"/></svg>
    <div class="t">Retirement Planning</div><div class="r">READ MORE</div>
  </div>
  <div class="abs svc-card" style="left:473px">
    <svg width="34" height="32" viewBox="0 0 34 32" fill="none" stroke="var(--blue)" stroke-width="1.8"><path d="M4 28h26"/><rect x="6" y="18" width="4" height="10"/><rect x="14" y="13" width="4" height="15"/><rect x="22" y="8" width="4" height="20"/><path d="M6 12l8-6 6 4 8-7"/></svg>
    <div class="t">Wealth Management</div><div class="r">READ MORE</div>
  </div>
  <div class="abs svc-card" style="left:812px">
    <svg width="34" height="32" viewBox="0 0 34 32" fill="none" stroke="var(--blue)" stroke-width="1.8"><rect x="6" y="4" width="20" height="24" rx="2"/><path d="M10 11h12M10 16h12M10 21h8"/></svg>
    <div class="t">Estate Planning</div><div class="r">READ MORE</div>
  </div>

  <svg class="abs arrow" style="left:64px;top:308px" viewBox="0 0 22 22" fill="none" stroke="#fff" stroke-width="1.6"><path d="M19 11H4M9 6l-5 5 5 5"/></svg>
  <svg class="abs arrow" style="left:1113px;top:308px" viewBox="0 0 22 22" fill="none" stroke="#fff" stroke-width="1.6"><path d="M3 11h15M13 6l5 5-5 5"/></svg>
  <div class="abs btn">GET IN TOUCH</div>
  <div class="abs dot" style="left:492px"></div>
  <div class="abs dot" style="left:506px"></div>
  <div class="abs dot" style="left:520px;background:#9fb0c9"></div>
  <div class="abs dot" style="left:534px"></div>
</section>

<section class="mission">
  <svg class="abs" style="left:0;top:0" width="1200" height="568" aria-hidden="true">
    <polygon points="0,0 210,0 0,270" fill="var(--pale)" opacity=".7"/>
    <polygon points="1120,430 1200,300 1200,568 1040,568" fill="var(--pale)" opacity=".8"/>
  </svg>
  <div class="abs label">Our Mission</div>
  <div class="abs h2">Empowering Individuals And Families To Achieve Financial Peace Of Mind And Prosperity.</div>
  <p class="abs para p1">At Summitline Wealth Management, we believe financial success is about more than numbers—it's about creating peace of mind. With &nbsp;years of experience], we are dedicated to guiding clients through every stage of their financial journey, from planning to legacy-building.</p>
  <p class="abs para p2">We are dedicated to building trusted relationships and delivering personalized solutions to help you achieve your goals, whether planning for retirement or creating a legacy.</p>
  <div class="abs btn">LEARN MORE</div>
  <div class="abs photo" role="img" aria-label="Photo of a hand with a pencil reviewing printed bar charts" style="left:786px;top:142px;width:312px;height:227px;background:linear-gradient(135deg,#eef1f5,#a9bad0)"></div>
  <div class="abs photo" role="img" aria-label="Photo of trading screens showing market graphs" style="left:569px;top:274px;width:173px;height:158px;background:linear-gradient(135deg,#27456e,#7e9cc4)"></div>
  <div class="abs photo" role="img" aria-label="Photo of a desk with financial reports and a keyboard" style="left:692px;top:303px;width:236px;height:203px;background:linear-gradient(135deg,#8c949e,#d5d9de)"></div>
</section>

<section class="benefits">
  <div class="abs label">Why Choose Us</div>
  <div class="abs h2">Our Benefits</div>
  <div class="abs ben" style="left:100px">
    <div class="ic"><svg width="32" height="32" viewBox="0 0 32 32" fill="none" stroke="#fff" stroke-width="1.8"><rect x="7" y="5" width="18" height="22" rx="2"/><path d="M11 11h10M11 16h10M11 21h6"/></svg></div>
    <div class="t">Tailored Financial Plans</div>
    <div class="d">Lorem Ipsum is simply dummy text of the printing and typesetting industry.</div>
  </div>
  <div class="abs ben" style="left:354px">
    <div class="ic"><svg width="32" height="32" viewBox="0 0 32 32" fill="none" stroke="#fff" stroke-width="1.8"><circle cx="16" cy="12" r="6"/><path d="M6 27c2-6 6-8 10-8s8 2 10 8"/></svg></div>
    <div class="t">Trusted Expertise</div>
    <div class="d">Lorem Ipsum is simply dummy text of the printing and typesetting industry.</div>
  </div>
  <div class="abs ben" style="left:608px">
    <div class="ic"><svg width="32" height="32" viewBox="0 0 32 32" fill="none" stroke="#fff" stroke-width="1.8"><circle cx="10" cy="11" r="4"/><circle cx="22" cy="11" r="4"/><path d="M3 25c1-5 4-7 7-7s6 2 7 7M15 25c1-5 4-7 7-7s6 2 7 7"/></svg></div>
    <div class="t">Lifetime Support</div>
    <div class="d">Lorem Ipsum is simply dummy text of the printing and typesetting industry.</div>
  </div>
  <div class="abs ben" style="left:862px">
    <div class="ic"><svg width="32" height="32" viewBox="0 0 32 32" fill="none" stroke="#fff" stroke-width="1.8"><path d="M5 27h22"/><rect x="8" y="18" width="3" height="9"/><rect x="14" y="14" width="3" height="13"/><rect x="20" y="10" width="3" height="17"/><circle cx="22" cy="5" r="2"/></svg></div>
    <div class="t">Personalized Approach</div>
    <div class="d">Lorem Ipsum is simply dummy text of the printing and typesetting industry.</div>
  </div>
</section>

<section class="team">
  <svg class="abs" style="left:0;top:0" width="1200" height="582" aria-hidden="true">
    <polygon points="0,0 215,0 0,280" fill="var(--pale)" opacity=".7"/>
    <polygon points="1105,100 1200,270 1200,582 1010,582" fill="var(--pale)" opacity=".8"/>
  </svg>
  <div class="abs label">About Summitline Wealth Management</div>
  <div class="abs h2">Who We Are</div>
  <div class="abs member" style="left:100px">
    <div class="ph photo" role="img" aria-label="Portrait photo of team member Owen Marlow in a navy suit" style="background:linear-gradient(135deg,#e9edf2,#9aa7b8)"></div>
    <div class="bar">Owen Marlow &nbsp;| <small>Ceo &amp; Founder</small></div>
  </div>
  <div class="abs member" style="left:354px">
    <div class="ph photo" role="img" aria-label="Portrait photo of team member Clara Benning in business attire" style="background:linear-gradient(135deg,#e3e3e0,#8f9093)"></div>
    <div class="bar">Clara Benning &nbsp;| <small>Founder</small></div>
  </div>
  <div class="abs member" style="left:608px">
    <div class="ph photo" role="img" aria-label="Portrait photo of team member Dev Harlan outdoors" style="background:linear-gradient(135deg,#7f8890,#3a4048)"></div>
    <div class="bar">Dev Harlan &nbsp;| Manager</div>
  </div>
  <div class="abs member" style="left:864px">
    <div class="ph photo" role="img" aria-label="Portrait photo of team member Theo Ramsey holding a phone" style="background:linear-gradient(135deg,#d8d4cd,#8e949c)"></div>
    <div class="bar">Theo Ramsey &nbsp;| Accountent</div>
    <div class="s" style="top:12px"></div>
    <div class="s" style="top:42px"></div>
    <div class="s" style="top:72px"></div>
    <div class="s" style="top:102px"></div>
  </div>
  <svg class="abs arrow" style="left:64px;top:301px" viewBox="0 0 22 22" fill="none" stroke="var(--ink)" stroke-width="1.6"><path d="M19 11H4M9 6l-5 5 5 5"/></svg>
  <svg class="abs arrow" style="left:1113px;top:301px" viewBox="0 0 22 22" fill="none" stroke="var(--ink)" stroke-width="1.6"><path d="M3 11h15M13 6l5 5-5 5"/></svg>
  <div class="abs join"><span>Want To Join Our Team?</span> We're Always Looking For Awesome People Who Can Bring New Perspectives.</div>
</section>

<section class="contact">
  <div class="abs frame"></div>
  <div class="abs img photo" role="img" aria-label="Photo of a smiling support advisor wearing a headset" style="background:linear-gradient(135deg,#eef0f3,#9ea9b8)"></div>
  <div class="abs label">Get In Touch</div>
  <div class="abs h2">Contact Us</div>
  <div class="abs field" style="left:601px;top:207px;width:241px">First Name</div>
  <div class="abs field" style="left:855px;top:207px;width:243px">Last Name</div>
  <div class="abs field" style="left:601px;top:256px;width:241px">Email</div>
  <div class="abs field" style="left:855px;top:256px;width:243px">Phone</div>
  <div class="abs field" style="left:601px;top:305px;width:497px;height:119px">Message</div>
  <div class="abs submit">SUBMIT NOW</div>
</section>

<footer>
  <div class="abs fbrand-mark"></div>
  <div class="abs fbrand">SUMMITLINE WEALTH<br>MANAGEMENT</div>
  <div class="abs fsoc" style="left:100px"></div>
  <div class="abs fsoc" style="left:131px"></div>
  <div class="abs fsoc" style="left:162px"></div>
  <div class="abs fsoc" style="left:194px"></div>

  <div class="abs fh" style="left:392px">Quick links</div>
  <div class="abs flink" style="top:91px">Home</div>
  <div class="abs flink" style="top:118px">Who We Are</div>
  <div class="abs flink" style="top:146px">Our Expertise &amp; Services</div>
  <div class="abs flink" style="top:173px">Our Team</div>
  <div class="abs flink" style="top:201px">Success Stories &amp; News</div>
  <div class="abs flink" style="top:228px">Contact Us</div>

  <div class="abs fh" style="left:597px">Contact Info</div>
  <div class="abs finfo" style="top:89px"><span class="ci"><svg width="11" height="11" viewBox="0 0 12 12" fill="#fff"><path d="M2 1l2 0 1 3-1.5 1a6 6 0 0 0 3.5 3.5L8 7l3 1v2c0 1-1 1-1 1C5 11 1 7 1 2c0 0 0-1 1-1z"/></svg></span><span style="padding-top:2px">555-014-2270</span></div>
  <div class="abs finfo" style="top:126px"><span class="ci"><svg width="11" height="9" viewBox="0 0 12 10" fill="none" stroke="#fff" stroke-width="1.3"><rect x="1" y="1" width="10" height="8"/><path d="M1 1l5 4 5-4"/></svg></span><span style="padding-top:2px">info@summitlinewealth.com</span></div>
  <div class="abs finfo" style="top:162px"><span class="ci"><svg width="10" height="12" viewBox="0 0 10 12" fill="none" stroke="#fff" stroke-width="1.3"><path d="M5 11S1 7 1 4.5a4 4 0 0 1 8 0C9 7 5 11 5 11z"/><circle cx="5" cy="4.5" r="1.4"/></svg></span><span>Lorem Ipsum is simply dummy<br>industry. 115 56 simple industry.</span></div>

  <div class="abs fh" style="left:872px">Subscribe Newsletter</div>
  <div class="abs fin">Email</div>
  <div class="abs fsub">SUBSCRIBE NOW</div>

  <div class="abs fline"></div>
  <div class="abs copy">© Copyright All Right Reserved.2024</div>
</footer>

</body>
</html>
```